The Regional Coverage Dealer Handbook

I am writing a best practice book for commercial lines insurance brokers. The subtitle is When The Path Bends Keep Walking Onward. So I want a graphic of maybe someone hiking the summit. I posted an example but don't feel limited I just foudn something I liked.

This is a business book

I just mocked up an example. I dont want designers limited by my design. I am looking for juggling to be artistically displayed on the front cover. I incorporated my name into the logo but probably dont want that in my final design. Should just have my name and designations Mark Toldavo, AAi, CWCP

Target Market(s)

Commercial Insurance Agents

Industry/Entity Type

Insurance

Font styles to use
Sans Serif

Colors

Designer to choose only greyscale colors for use in the design.

Requirements
Must have
• Must have the title of the book
The Regional
Coverage Dealer
Handbook

Also the sub title When The Path Bends Keep Walking Onward

My Name on front cover Mark Toldavo, AAI, CWCP

Book Cover should be black. I uploaded a copy of my work comp playbook for my desired color scehme.

My Lantern Logo on front cover and TideMarket logo on back cover
Nice to have
• Color should be black gray adn red using color from my logo.

```html
<!DOCTYPE html>
<html lang="en">
<head>
<meta charset="utf-8">
<title>The Regional Coverage Dealer Handbook</title>
<link href="https://fonts.googleapis.com/css2?family=Montserrat:wght@400;700&family=Oswald:wght@700&family=Open+Sans:wght@400;600&display=swap" rel="stylesheet">
<style>
  :root {
    --cover-dark: #1f2a30;
    --wall-warm: #9c7f72;
    --glow: #f6ebe2;
    --door-top: #2a3236;
    --door-mid: #c8924a;
    --door-low: #f2e7d8;
    --floor-light: #c9c6c3;
    --floor-dark: #4a4c4e;
    --title-red: #d6261c;
    --title-shadow: #3a0d0a;
    --text-light: #ffffff;
    --text-dark: #141414;
  }
  html, body {
    margin: 0;
    padding: 0;
    width: 840px;
    height: 1200px;
    overflow: hidden;
    background: var(--cover-dark);
  }
  .cover {
    position: relative;
    width: 840px;
    height: 1200px;
    overflow: hidden;
    background: var(--cover-dark);
  }
  .cover-scene {
    position: absolute;
    inset: 0;
  }
  .scene-wall {
    position: absolute;
    inset: 0;
    background:
      radial-gradient(ellipse 330px 420px at 420px 880px, rgba(246,235,226,0.95) 0%, rgba(200,160,145,0.6) 40%, rgba(156,127,114,0) 100%),
      linear-gradient(180deg, var(--cover-dark) 0%, var(--cover-dark) 38%, #3a3d3e 62%, #5a4c47 80%, #6a5a54 100%);
  }
  .scene-doorway {
    position: absolute;
    left: 312px;
    width: 200px;
    top: 184px;
    height: 790px;
    background: linear-gradient(180deg, var(--door-top) 0%, #4a4a44 25%, var(--door-mid) 50%, #e9c58c 70%, var(--door-low) 100%);
    opacity: 0.9;
  }
  .scene-floor {
    position: absolute;
    left: 0;
    right: 0;
    top: 972px;
    bottom: 0;
    background:
      radial-gradient(ellipse 360px 140px at 420px 0px, rgba(235,228,222,0.95) 0%, rgba(201,198,195,0.6) 50%, rgba(201,198,195,0) 100%),
      linear-gradient(180deg, #8d8a88 0%, var(--floor-dark) 100%);
  }
  .title {
    position: absolute;
    left: 46px;
    right: 40px;
    top: 108px;
    margin: 0;
    color: var(--title-red);
    text-shadow: 3px 3px 0 var(--title-shadow);
    text-transform: uppercase;
    line-height: 1;
  }
  .title-line { display: block; white-space: nowrap; }
  .title-top {
    font-family: "Montserrat", sans-serif;
    font-weight: 700;
    font-size: 90px;
    letter-spacing: -1px;
  }
  .title-main {
    font-family: "Oswald", sans-serif;
    font-weight: 700;
    font-size: 170px;
    line-height: 0.9;
    margin-top: 4px;
    letter-spacing: -2px;
  }
  .title-bottom {
    font-family: "Montserrat", sans-serif;
    font-weight: 400;
    font-size: 68px;
    margin-top: 12px;
    letter-spacing: -1px;
  }
  .subtitle {
    position: absolute;
    left: 50%;
    top: 486px;
    transform: translateX(-50%);
    margin: 0;
    padding: 2px 8px;
    background: rgba(40,48,52,0.55);
    color: var(--text-light);
    font-family: "Open Sans", sans-serif;
    font-size: 29px;
    white-space: nowrap;
  }
  .author {
    position: absolute;
    left: 0;
    right: 0;
    top: 1024px;
    margin: 0;
    text-align: center;
    font-family: "Open Sans", sans-serif;
    font-weight: 600;
    font-size: 31px;
    letter-spacing: -1px;
    color: var(--text-dark);
  }
  .brand {
    position: absolute;
    left: 0;
    right: 0;
    top: 1074px;
    display: flex;
    justify-content: center;
    align-items: center;
    gap: 18px;
  }
  .brand-mark {
    width: 30px;
    height: 30px;
    border-radius: 50%;
    background: var(--title-red);
  }
  .brand-name {
    font-family: "Open Sans", sans-serif;
    font-weight: 400;
    font-size: 52px;
    letter-spacing: 14px;
    color: var(--text-dark);
  }
</style>
</head>
<body>
<main class="cover">
  <div class="cover-scene" role="img" aria-label="Photograph of a businessman seen from behind, arms raised in triumph, standing before a tall glowing doorway that opens onto a night city street">
    <div class="scene-wall"></div>
    <div class="scene-doorway"></div>
    <div class="scene-floor"></div>
  </div>
  <h1 class="title">
    <span class="title-line title-top">The Regional</span>
    <span class="title-line title-main">Coverage</span>
    <span class="title-line title-bottom">Dealer Handbook</span>
  </h1>
  <p class="subtitle">When The Path Bends Keep Walking Onward</p>
  <p class="author">MARK TOLDAVO, AAI, CWCP</p>
  <div class="brand">
    <span class="brand-mark"></span>
    <span class="brand-name">LANTERN</span>
  </div>
</main>
</body>
</html>
```